Elm Ridge Baptist Church sign

We want a colourful, attractive sign that includes connection to being a Christian Church living in the foothills of the Canadian Rocky Mountains. As far as printed words, we need it to say “ Elm Ridge Baptist Church”. We are planning on a sign that is 6’ x 4’. Our church slogan is:
“ Live like Jesus, Love like Jesus”. This slogan could be included on the sign if space allows. To all designers; in talking with the communications team at our church, we want to eliminate the church’s slogan “ live like Jesus, live like Jesus “, from being on the sign.

```html
<!DOCTYPE html>
<html lang="en">
<head>
<meta charset="utf-8">
<title>Elm Ridge Baptist Church Sign</title>
<link href="https://fonts.googleapis.com/css2?family=Cinzel:wght@400;700;800&display=swap" rel="stylesheet">
<style>
  :root {
    --backdrop: #c8c8c8;
    --sign-yellow: #fff200;
    --title-red: #e8202a;
    --ink: #111111;
    --ornament-tone: #e4dc4a;
    --valley-haze: #e6e23a;
    --valley-green: #9fb04a;
    --field-green: #7f9a3e;
  }
  * { margin: 0; padding: 0; box-sizing: border-box; }
  html, body { width: 1200px; height: 1200px; overflow: hidden; }
  body {
    background: var(--backdrop);
    display: flex;
    align-items: center;
    justify-content: center;
  }
  .sign {
    position: relative;
    width: 1032px;
    height: 688px;
    background: var(--sign-yellow);
    overflow: hidden;
  }
  .valley-photo {
    position: absolute;
    left: 0; right: 0; bottom: 0;
    height: 62%;
    background: linear-gradient(to bottom,
      rgba(230,226,58,0) 0%,
      var(--valley-haze) 18%,
      #c9cc3c 45%,
      var(--valley-green) 72%,
      var(--field-green) 100%);
  }
  .corner-ornament {
    position: absolute;
    top: 0;
    width: 175px;
    height: 175px;
    background: var(--ornament-tone);
  }
  .corner-ornament.left { left: 0; border-bottom-right-radius: 100%; }
  .corner-ornament.right { right: 0; border-bottom-left-radius: 100%; }
  .lettering {
    position: absolute;
    inset: 0;
    text-align: center;
    font-family: 'Cinzel', serif;
    line-height: 1;
  }
  .church-name {
    position: absolute;
    top: 95px;
    width: 100%;
    font-size: 88px;
    font-weight: 400;
    color: var(--title-red);
  }
  .divider {
    position: absolute;
    top: 218px;
    left: 317px;
    width: 395px;
    height: 22px;
  }
  .denomination {
    position: absolute;
    top: 280px;
    width: 100%;
    font-size: 76px;
    font-weight: 400;
    color: var(--ink);
  }
  .building-type {
    position: absolute;
    top: 363px;
    width: 100%;
    font-size: 162px;
    font-weight: 700;
    letter-spacing: 3px;
    color: var(--ink);
  }
</style>
</head>
<body>
  <main class="sign">
    <div class="valley-photo" role="img" aria-label="Photograph of a foothills valley with forest, town and the church building beneath distant mountains"></div>
    <div class="corner-ornament left" role="img" aria-label="Decorative scroll flourish in the top left corner"></div>
    <div class="corner-ornament right" role="img" aria-label="Decorative scroll flourish in the top right corner"></div>
    <div class="lettering">
      <h1 class="church-name">Elm Ridge</h1>
      <svg class="divider" viewBox="0 0 395 22" aria-hidden="true">
        <line x1="8" y1="11" x2="387" y2="11" stroke="#111" stroke-width="2"/>
        <circle cx="6" cy="11" r="4" fill="#111"/>
        <circle cx="389" cy="11" r="4" fill="#111"/>
      </svg>
      <div class="denomination">Baptist</div>
      <div class="building-type">CHURCH</div>
    </div>
  </main>
</body>
</html>
```